Dutch craft distillery needs labels designed for Gin bottle

We are a small craft distillery based in The Netherlands. We are currently producing only GIN. While we do have a logo for our distillery, we are still in search of a winning design for our Gin bottle. We are looking for something modern yet classy. Let your creativity run wild. Play around with colours, think out of the box….The winning designer will be challenged to create the coolest labels for the different flavours of Gin we will be producing in the near future. The label will maintain the same design elements throughout the design, but will also be able to differentiate each variety clearly. So for e.g. A flowery Vantoor Gin can have a pink label with a different description and a spicy Vantoor gin can have another colour with another description and so on. If the design really appeals to us, we might also invite the designer to do our website for us!

In a nutshell: It is a 500 ml bottle, (Please check the attachment so you get an idea as to what kind of bottle to imagine while making the labels). The bottle is going to have a light coloured wooden lid/cork to it. As of now we have a transparent seal to complete the sealing process once the bottling is done. The idea is that we will have two labels. One in the front and one behind. The size of the labels are as follows:

Front label: 102 x 76 mm the front label. (TO BE USED HORIZONTALLY). The details that we need on the front label are in a separate attachment.

Back label: The size for the label at the back of the bottle is: 76 x 51 mm (TO BE USED VERTICALLY) The information that needs to come on the label behind is also in the same document which is attached separately. The label behind will also have batch no. & date (Please refer to attachment to understand what I mean by batch no. date, distiller’s signature etc.) I have attached a picture of an already existing brand which has its batch number and distillers signature etc on it….so you can understand what I exactly mean by that. Please do not copy their design, this is purely to give you an idea as to what I mean by batch number and so on. The address of the distillery can be put horizontally, vertically, on the side along one border, or however you find appropriate. This is the address:
Klaverhoekstraat 41,
6318 KT, Hengelo.
The Netherlands.
www.vantoor.nl

Logo’s no drinking when pregnant, No driving and drinking, No drinking under the age of 18 need to be present on the label behind. Alternately, we can also have www.calm-sipping.com instead of the under 18 no alcohol sign, most alcohol bottles these days have it. Please let me know what else you would need from me for this. So be creative and do your best!

Thanks and regards, Marisol Vendekampa.

Target Market(s)

Largely males and females between 25-55 , the audience could even be slightly older.

Colors

Designer to choose colors to be used in the design.

Requirements
Must have
• 1) The labels need to be modern, yet classy, elite..
• 2) We need to specify the fact that we are a craft distillery and the gin is HANDMADE, using only the highest quality ingredients.
• 3) We at Vantoor live, breathe, dream, talk about our dream which is our distillery and its product. The label needs to bring home this point and should clearly specify and mention that it is produced and bottled in The Netherlands. Or handmade and bottled with love and passion in The Netherlands or something to that effect if it matches with the rest of the design.
• 4) The colours you chose must match in some way or the other with the colours used for the logo design.
Nice to have
• Would be nice to have colours and look bold, although not completely necessary.
Should not have
• What I definitely do not want is something too whacky like a skull or some kind of vague work of art. For the rest, I leave it upto you….!

```html
<!DOCTYPE html>
<html lang="en">
<head>
<meta charset="utf-8">
<title>Vantoor Gin – Front Label</title>
<link href="https://fonts.googleapis.com/css2?family=Rozha+One&family=Cinzel:wght@400;500;600&family=Oswald:wght@300&display=swap" rel="stylesheet">
<style>
  :root {
    --ink: #141414;
    --panel: #232323;
    --stripe: #2c2c2c;
    --copper-dark: #7a3f1d;
    --copper: #c07a4a;
    --copper-light: #e9b48e;
    --cream: #f3e6d6;
    --white: #ffffff;
    --shadow-grey: #a9a9a9;
  }
  * { margin: 0; padding: 0; box-sizing: border-box; }
  html, body { width: 1200px; height: 893px; overflow: hidden; background: var(--ink); }
  .label {
    position: relative;
    width: 1200px; height: 893px;
    background: var(--ink);
  }
  .frame-outer {
    position: absolute; left: 13px; top: 15px; width: 1174px; height: 851px;
    border: 3px solid var(--copper);
    box-shadow: inset 0 0 0 6px var(--ink), inset 0 0 0 8px var(--copper-light);
  }
  .frame-inner {
    position: absolute; left: 34px; top: 40px; width: 1132px; height: 801px;
    border: 2px solid var(--copper);
  }
  .panel {
    position: absolute; left: 39px; top: 45px; width: 1122px; height: 791px;
    background: repeating-linear-gradient(to bottom, var(--panel) 0 6px, var(--stripe) 6px 9px);
  }
  .house-name {
    position: absolute; left: 0; width: 1200px; top: 108px; text-align: center;
    font-family: "Cinzel", serif; font-weight: 500; font-size: 24px; line-height: 1;
    color: var(--white); letter-spacing: 2px;
  }
  .brand-title {
    position: absolute; left: 163px; width: 862px; top: 188px; text-align: center;
    font-family: "Cinzel", serif; font-weight: 600; font-size: 176px; line-height: 1;
    color: var(--copper-light); letter-spacing: 6px; white-space: nowrap;
  }
  .product-art { position: absolute; left: 0; top: 0; width: 1200px; height: 893px; }
  .ribbon {
    position: absolute; left: 377px; top: 544px; width: 440px; height: 58px;
    background: var(--white); border: 4px solid var(--ink);
    outline: 2px solid var(--white);
    display: flex; align-items: center; justify-content: center;
  }
  .ribbon-text {
    font-family: "Oswald", sans-serif; font-weight: 300; font-size: 36px;
    color: var(--ink); letter-spacing: 0.5px; line-height: 1;
  }
  .maker-line {
    position: absolute; left: 0; width: 1200px; top: 613px; text-align: center;
    font-family: "Cinzel", serif; font-size: 13px; color: var(--white);
  }
  .claims {
    position: absolute; left: 0; width: 1200px; top: 682px; text-align: center;
    font-family: "Cinzel", serif; font-size: 21px; line-height: 30px; color: var(--white);
    letter-spacing: 0.5px;
  }
  .volume {
    position: absolute; left: 0; width: 1200px; top: 764px; text-align: center;
    font-family: "Cinzel", serif; font-size: 27px; color: var(--white);
  }
  .origin {
    position: absolute; left: 0; width: 1200px; top: 806px; text-align: center;
    font-family: "Cinzel", serif; font-size: 11px; color: var(--white);
  }
  .badge { position: absolute; left: 98px; top: 562px; width: 208px; height: 208px; }
  .windmill-art {
    position: absolute; left: 827px; top: 480px; width: 279px; height: 313px;
    background: linear-gradient(135deg, var(--cream), var(--copper) 70%, var(--copper-dark));
    opacity: 0.85; border-radius: 6px;
  }
</style>
</head>
<body>
<main class="label">
  <div class="frame-outer"></div>
  <div class="panel"></div>
  <div class="frame-inner"></div>

  <p class="house-name">Vantoor Distillery</p>

  <h1 class="brand-title">VANTOOR</h1>

  <svg class="product-art" viewBox="0 0 1200 893" aria-label="Gin">
    <text x="602" y="499" text-anchor="middle" font-family="'Rozha One', serif" font-size="160" fill="var(--shadow-grey)">GIN</text>
    <text x="596" y="494" text-anchor="middle" font-family="'Rozha One', serif" font-size="160" fill="var(--white)">GIN</text>
  </svg>

  <div class="ribbon"><span class="ribbon-text">PREMIUM LONDON DRY GIN</span></div>
  <p class="maker-line">DISTILLED AND BOTTLED BY VANTOOR DISTILLERY</p>

  <p class="claims">100% NATURAL BOTANICALS<br>NO ARTIFICIAL FLAVOURING</p>
  <p class="volume">50 CL | 43% VOL</p>
  <p class="origin">PRODUCT OF THE NETHERLANDS</p>

  <svg class="badge" viewBox="0 0 210 210" aria-label="Handcrafted small batch seal">
    <defs>
      <radialGradient id="discGlow" cx="0.4" cy="0.35" r="0.7">
        <stop offset="0" stop-color="#f6dcc2"/>
        <stop offset="1" stop-color="#b06a36"/>
      </radialGradient>
      <path id="arcTop" d="M 25 105 A 80 80 0 0 1 185 105"/>
      <path id="arcBottom" d="M 20 105 A 85 85 0 0 0 190 105"/>
    </defs>
    <circle cx="105" cy="105" r="102" fill="none" stroke="var(--copper)" stroke-width="1.5"/>
    <circle cx="105" cy="105" r="72" fill="url(#discGlow)" role="img" aria-label="Copper still illustration"/>
    <text font-family="Cinzel, serif" font-size="19" fill="var(--copper)" letter-spacing="4">
      <textPath href="#arcTop" startOffset="50%" text-anchor="middle">HANDCRAFTED</textPath>
    </text>
    <text font-family="Cinzel, serif" font-size="19" fill="var(--copper)" letter-spacing="3" dy="14">
      <textPath href="#arcBottom" startOffset="50%" text-anchor="middle">SMALL BATCH</textPath>
    </text>
  </svg>

  <div class="windmill-art" role="img" aria-label="Dutch windmill with tulips and fence illustration"></div>
</main>
</body>
</html>
```